Clear Plastic Card Design

I am looking to have a business card designed from my logo icon. I am looking to match the style of a different business card I have attached in the files.
Looking for a card that is plastic, with layers of transparency in the shape of my logo icon (also attached in the files) - not a circle like the other card. The winning design will incorporate the red icon logo on the front and back and include the charity's name, "Lanterns for the Weary" in the same or similar font, as well as an email and phone number. For now, use the email: email@lanternsfortheweary.org and the phone number 555-318-4072.
We like how the sample business card has transparency, partial and full opacity layers and a matching color scheme. Files will need to be in vector so that our business card printing company can work with it.
UPDATE:
We've some excellent designs in, thank you everyone! I got an early review from the owner, and he requested a minor redirect to find his perfect design. He wants the design to stand out by NOT being a rectangle. Try instead a circle, square, or best yet - something that falls in the outline of the logo icon, either fully or partially. Thank you, everyone!
Contact Information for Business Card
Lanterns for the Weary text should be incorporated as well as a phone and email.
Look and feel

```html
<!DOCTYPE html>
<html lang="en">
<head>
<meta charset="utf-8">
<title>Lanterns for the Weary — Plastic Business Card</title>
<link rel="stylesheet" href="https://fonts.googleapis.com/css2?family=Questrial&display=swap">
<style>
  :root {
    --page: #ffffff;
    --card-red: #c01a2a;
    --card-red-deep: #b3121f;
    --plastic-rim: rgba(192, 26, 42, 0.32);
    --plastic-mid: rgba(192, 26, 42, 0.6);
    --ink-light: #f7f3f3;
    --card-shadow: rgba(60, 10, 15, 0.2);
  }

  html, body {
    margin: 0;
    padding: 0;
    width: 1200px;
    height: 846px;
    overflow: hidden;
    background: var(--page);
    font-family: "Questrial", "Century Gothic", sans-serif;
  }

  .canvas {
    position: relative;
    width: 1200px;
    height: 846px;
  }

  .card {
    position: absolute;
    width: 520px;
    height: 298px;
    color: var(--ink-light);
    filter: drop-shadow(0 12px 20px var(--card-shadow));
  }

  .card--back  { left: 610px; top: 140px; }
  .card--front { left: 70px;  top: 410px; }

  .card__body {
    position: absolute;
    inset: 0;
    width: 520px;
    height: 298px;
  }

  .card__rim   { fill: var(--plastic-rim); }
  .card__layer { fill: var(--plastic-mid); }
  .card__panel { fill: url(#panel-red); }

  .lockup {
    position: absolute;
    display: flex;
    align-items: center;
    gap: 16px;
  }

  .card--back .lockup  { right: 50px; top: 140px; }
  .card--front .lockup { right: 50px; top: 70px; }

  .lockup__name {
    font-size: 27px;
    line-height: 1.05;
    letter-spacing: 0.5px;
    text-align: right;
    color: var(--ink-light);
    margin: 0;
    font-weight: 400;
  }

  .lockup__mark {
    width: 74px;
    height: 74px;
    background: var(--ink-light);
    flex: none;
  }

  .contact {
    position: absolute;
    left: 44px;
    bottom: 44px;
    margin: 0;
    font-size: 19px;
    line-height: 1.35;
    letter-spacing: 0.6px;
    font-style: normal;
  }

  .contact__line {
    display: block;
  }
</style>
</head>
<body>
  <svg width="0" height="0" aria-hidden="true" focusable="false" style="position:absolute">
    <defs>
      <linearGradient id="panel-red" x1="0" y1="0" x2="1" y2="1">
        <stop offset="0" stop-color="#c01a2a"/>
        <stop offset="1" stop-color="#b3121f"/>
      </linearGradient>
    </defs>
  </svg>

  <main class="canvas">
    <section class="card card--back" aria-label="Card back">
      <svg class="card__body" viewBox="0 0 520 298" aria-hidden="true">
        <path class="card__rim" d="M48,0 H520 V250 L472,298 H0 V48 Z"/>
        <path class="card__layer" d="M54,10 H510 V246 L468,288 H10 V54 Z"/>
        <path class="card__panel" d="M60,20 H500 V242 L464,278 H20 V60 Z"/>
      </svg>
      <div class="lockup">
        <h2 class="lockup__name">Lanterns for the<br>Weary</h2>
        <span class="lockup__mark" aria-hidden="true"></span>
      </div>
    </section>

    <section class="card card--front" aria-label="Card front">
      <svg class="card__body" viewBox="0 0 520 298" aria-hidden="true">
        <path class="card__rim" d="M48,0 H520 V250 L472,298 H0 V48 Z"/>
        <path class="card__layer" d="M54,10 H510 V246 L468,288 H10 V54 Z"/>
        <path class="card__panel" d="M60,20 H500 V242 L464,278 H20 V60 Z"/>
      </svg>
      <div class="lockup">
        <h1 class="lockup__name">Lanterns for the<br>Weary</h1>
        <span class="lockup__mark" aria-hidden="true"></span>
      </div>
      <address class="contact">
        <span class="contact__line">Phone: 555-318-4072</span>
        <span class="contact__line">email@lanternsfortheweary.org</span>
      </address>
    </section>
  </main>
</body>
</html>
```